Need DL Flyer for Real Estate Drops

We need a real estate flyer ,double sided. With content on 1 side like: Want to know what's your house is worth " contact us today and on other side agent details. We are looking for an ongoing partnership with designer so this assignment will be ongoing

```html
<!DOCTYPE html>
<html lang="en">
<head>
<meta charset="utf-8">
<title>Dunmore Real Estate – DL Flyer</title>
<link rel="stylesheet" href="https://fonts.googleapis.com/css2?family=Bitter:wght@700;800&family=Montserrat:wght@300;400;500&family=Playfair+Display:wght@900&display=swap">
<style>
  :root{
    --navy:#0b1e33;
    --red:#c90000;
    --slate:#56636f;
    --white:#ffffff;
    --stage:#cccccc;
  }
  *{margin:0;padding:0;box-sizing:border-box}
  html,body{width:1200px;height:1200px;overflow:hidden;background:var(--stage)}
  .stage{position:relative;width:1200px;height:1200px}
  .flyer{position:absolute;top:106px;width:480px;height:988px;overflow:hidden;background:var(--navy)}
  .flyer--front{left:80px}
  .flyer--back{left:653px}
  .flyer__shapes{position:absolute;inset:0}
  .abs{position:absolute}

  /* front */
  .brand__mark{left:84px;top:38px;width:78px;height:78px;background:var(--red)}
  .brand__name{left:196px;top:34px;font:500 52px/1 "Montserrat",sans-serif;color:var(--white);letter-spacing:-1px}
  .brand__tag{left:230px;top:100px;font:400 14px/1 "Montserrat",sans-serif;color:var(--white);letter-spacing:4px}
  .headline{left:36px;top:172px;font:800 35px/53px "Bitter",serif;color:var(--white);white-space:nowrap}
  .price-mark{left:144px;top:270px;font:900 210px/1 "Playfair Display",serif;color:var(--white);letter-spacing:6px}
  .cta{left:26px;top:814px;font:800 31px/42px "Bitter",serif;color:var(--white);white-space:nowrap}

  /* back */
  .agent__name{left:253px;top:26px;font:300 40px/1 "Montserrat",sans-serif;color:var(--white)}
  .agent__bio{left:269px;top:78px;width:200px;font:400 12px/15.6px "Montserrat",sans-serif;color:var(--white)}
  .agent__note{left:269px;top:207px;width:205px;font:400 12px/15.6px "Montserrat",sans-serif;color:var(--white)}
  .stats{left:55px;top:316px;list-style:none}
  .stats li{height:41px;display:flex;align-items:center;font:400 12px/1 "Montserrat",sans-serif;color:var(--white)}
  .stats__label{width:216px}
  .stats__value{font:700 23px/1 "Bitter",serif}
  .pitch{left:23px;top:479px;width:260px;font:700 11.2px/15.6px "Bitter",serif;color:var(--white);text-transform:uppercase}
  .contact{font:400 17px/1 "Montserrat",sans-serif;color:var(--white)}
  .contact--address{left:177px;top:818px}
  .contact--email{left:180px;top:846px}
  .contact--phone{left:178px;top:874px;font-size:40px;letter-spacing:0}
</style>
</head>
<body>
<main class="stage">

  <!-- Front side -->
  <section class="flyer flyer--front">
    <svg class="flyer__shapes" width="480" height="988" viewBox="0 0 480 988">
      <defs>
        <linearGradient id="tabletScene" x1="0" y1="0" x2="1" y2="1">
          <stop offset="0" stop-color="#e8ecf1"/>
          <stop offset="0.55" stop-color="#9aa8ba"/>
          <stop offset="1" stop-color="#5a6672"/>
        </linearGradient>
      </defs>
      <rect x="0" y="0" width="480" height="13" fill="var(--white)"/>
      <!-- red field with rounded upper-left corner -->
      <path d="M0,422 C30,330 100,292 184,292 L480,292 L480,950 Q480,962 468,962 L0,962 Z" fill="var(--red)"/>
      <!-- white stepped panel -->
      <path d="M256,460 L480,460 L480,627 L432,627 C432,722 390,794 318,794 L0,794 L0,627 L108,627 C108,530 170,460 256,460 Z" fill="var(--white)"/>
      <!-- photo area -->
      <path d="M0,627 L108,627 L110,600 C118,582 134,567 152,560 L392,560 C398,640 375,715 330,760 L300,790 L0,790 Z" fill="url(#tabletScene)" role="img" aria-label="Hand holding a tablet with a two-storey house model on it"/>
      <!-- arrow -->
      <rect x="404" y="814" width="18" height="124" fill="var(--white)"/>
      <polygon points="420,800 468,876 420,962" fill="var(--white)"/>
    </svg>

    <div class="abs brand__mark"></div>
    <div class="abs brand__name">dunmore</div>
    <div class="abs brand__tag">REAL ESTATE</div>

    <h1 class="abs headline">WANT TO KNOW WHAT’S<br>YOUR HOUSE IS WORTH ?</h1>
    <div class="abs price-mark">$?</div>
    <p class="abs cta">CONTACT US TODAY AND<br>ON OTHER SIDE AGENT<br>DETAILS</p>
  </section>

  <!-- Back side -->
  <section class="flyer flyer--back">
    <svg class="flyer__shapes" width="480" height="988" viewBox="0 0 480 988">
      <defs>
        <linearGradient id="portraitScene" x1="0" y1="0" x2="0" y2="1">
          <stop offset="0" stop-color="#b9cde0"/>
          <stop offset="0.45" stop-color="#7a8ea4"/>
          <stop offset="1" stop-color="#3f4650"/>
        </linearGradient>
        <linearGradient id="dealScene" x1="0" y1="0" x2="0" y2="1">
          <stop offset="0" stop-color="#9ea3a6"/>
          <stop offset="0.6" stop-color="#6f7a70"/>
          <stop offset="1" stop-color="#4f7a34"/>
        </linearGradient>
      </defs>
      <rect x="0" y="0" width="224" height="13" fill="var(--white)"/>
      <rect x="0" y="13" width="224" height="283" fill="url(#portraitScene)" role="img" aria-label="Portrait of the agent in a suit by the waterfront"/>
      <path d="M224,202 L480,202 L480,306 L170,306 C200,292 220,265 224,232 Z" fill="var(--red)"/>
      <path d="M0,296 L150,296 L170,306 L330,306 C420,306 480,360 480,430 L480,962 L170,962 C80,962 20,930 0,880 Z" fill="var(--slate)"/>
      <path d="M0,462 L310,462 C360,462 383,540 383,626 L0,626 Z" fill="var(--red)"/>
      <path d="M55,626 L480,626 L480,794 L150,794 C100,760 60,690 55,626 Z" fill="url(#dealScene)" role="img" aria-label="Two business people shaking hands in front of a house"/>
      <rect x="127" y="872" width="353" height="46" fill="var(--red)"/>

      <!-- team icon -->
      <g fill="var(--white)">
        <circle cx="245" cy="239" r="5"/><circle cx="234" cy="243" r="4"/><circle cx="256" cy="243" r="4"/>
        <path d="M236,260 Q236,247 245,247 Q254,247 254,260 Z"/>
        <path d="M226,258 Q226,249 233,249 Q236,249 237,251 Q233,254 233,258 Z"/>
        <path d="M264,258 Q264,249 257,249 Q254,249 253,251 Q257,254 257,258 Z"/>
      </g>

      <!-- ticks -->
      <g>
        <path d="M23,322 h24 v24 l-12,6 l-12,-6 Z" fill="var(--white)"/>
        <path d="M28,334 l5,5 l9,-10" stroke="var(--slate)" stroke-width="2.6" fill="none"/>
        <path d="M23,364 h24 v24 l-12,6 l-12,-6 Z" fill="var(--white)"/>
        <path d="M28,376 l5,5 l9,-10" stroke="var(--slate)" stroke-width="2.6" fill="none"/>
        <path d="M23,404 h24 v24 l-12,6 l-12,-6 Z" fill="var(--white)"/>
        <path d="M28,416 l5,5 l9,-10" stroke="var(--slate)" stroke-width="2.6" fill="none"/>
      </g>

      <!-- contact icons -->
      <path d="M142,816 a8,8 0 0 1 8,8 c0,6 -8,14 -8,14 c0,0 -8,-8 -8,-14 a8,8 0 0 1 8,-8 Z" fill="var(--white)"/>
      <circle cx="142" cy="824" r="3" fill="var(--slate)"/>
      <rect x="132" y="847" width="20" height="14" rx="1.5" fill="var(--white)"/>
      <path d="M132,848 l10,7 l10,-7" stroke="var(--slate)" stroke-width="1.6" fill="none"/>
      <path d="M137,877 l7,-2 l5,10 l-4,3 c2,6 6,10 12,13 l3,-4 l10,5 l-2,7 c-18,1 -33,-14 -31,-32 Z" fill="var(--white)"/>

      <!-- social placeholders -->
      <g fill="var(--white)">
        <circle cx="253" cy="942" r="10"/>
        <circle cx="311" cy="942" r="10"/>
        <circle cx="369" cy="942" r="10"/>
        <circle cx="427" cy="942" r="10"/>
      </g>
    </svg>

    <h2 class="abs agent__name">John Doe</h2>
    <p class="abs agent__bio">Velit quis duis est: Deserunt nulla ullamco do in. Eu dolore mollit cupidatat do tempor. Veniam fugiat labore amet non id, ut pariatur nisi ex magna dolore qui mollit ea.</p>
    <p class="abs agent__note">Dolor id qui anim lorem qui excepteur in, in ad duis? Eiusmod, qui pariatur aliqua ut mollit, excepteur deserunt, dolore veniam magna elit.</p>

    <ul class="abs stats">
      <li><span class="stats__label">DOLOR ID QUI ANIM LOREM QUI</span><span class="stats__value">150</span></li>
      <li><span class="stats__label">DOLOR ID QUI ANIM LOREM QUI</span><span class="stats__value">260</span></li>
      <li><span class="stats__label">DOLOR ID QUI ANIM LOREM QUI</span><span class="stats__value">70</span></li>
    </ul>

    <p class="abs pitch">Exercitation, ut amet est esse est sint, tempor incididunt tempor est velit, ex aliquip eu. Veniam et ad. Eiusmod ut et duis minim eu, anim adipisicing ut consectetur sit commodo occaecat, enim incididunt dolore. Cillum nisi ut quis consequat tempor ad dolore velit, est exercitation irure ex et commodo ullamco.</p>

    <p class="abs contact contact--address">48 Harbor Ln, Lakeview NC 27010</p>
    <p class="abs contact contact--email">office@dunmorerealestate.com</p>
    <p class="abs contact contact--phone">555-014-2288</p>
  </section>

</main>
</body>
</html>
```